Harbor Quill is a Smart Device and Wiring Business offering the latest in Smart Home Devices inc

Looking for a new website to draw people to my business and explain what a smart home is all about. I currently own a domain and have a website I put together in webnimbus business website builder. address www.harborquill.com. The website needs modernising and be visually appealing with cool action buttons, client feedback page etc.

The webpage needs to present an image of seamless integration of wireless voice control and smart devices that take tasks and activities away from the owner saving them time and money.

I have a chatterbay business page(harbor quill) and snapmeadow linked with the business, are we able to link this to the website somehow?

Target Market(s)

Residential home owners who want to modernise their home. Who have seen adverts for orbit nook and kestrel nova and want to put it in their home.

Industry/Entity Type

Technology Equipment

Number of Pages Required

1 page

Colors

Designer to choose colors to be used in the design.

Requirements
Must have
• A great landing page, that is modern and attractive, that gets across the idea of smart devices and technology.
• Must be ios/android device friendly.
Nice to have
• interactive/animated buttons
• I like the direction and interactiveness of these websites, a simplified version would be awesome.
• Something in between:
• http://www.oakridgelofts.com/ and https://plumcove.com/
• http://www.oakridgelofts.com/

```html
<!DOCTYPE html>
<html lang="en">
<head>
<meta charset="utf-8">
<title>Harbor Quill — Smart Device Integration</title>
<link rel="stylesheet" href="https://fonts.googleapis.com/css2?family=Jost:wght@400;500;600&family=Mulish:wght@400;600;700&display=swap">
<style>
:root{
  --brand:#2a9fd6;
  --brand-deep:#0d8ccc;
  --ink:#2b2b2b;
  --muted:#6b6b6b;
  --panel:#e9e9e9;
  --caption:#efefef;
  --footer:#1b1f27;
  --white:#ffffff;
}
*{box-sizing:border-box;margin:0;padding:0}
html,body{width:1200px;height:2406px;overflow:hidden}
body{position:relative;background:var(--white);font-family:"Mulish",sans-serif;color:var(--ink)}
.abs{position:absolute}

/* header */
.site-header{left:0;top:0;width:1200px;height:96px;background:var(--white)}
.brand{left:22px;top:26px;display:flex;align-items:center;gap:10px}
.brand-mark{width:44px;height:44px;border-radius:50%;background:var(--brand)}
.brand-name{font-family:"Jost",sans-serif;font-weight:500;font-size:22px;color:var(--brand);line-height:1}
.main-nav{left:655px;top:0;height:96px;display:flex;align-items:center;gap:0}
.main-nav a{font-size:11px;color:var(--ink);text-decoration:none;padding:0 12px;height:96px;line-height:96px;position:relative}
.main-nav a.is-active{color:var(--brand)}
.main-nav a.is-active::after{content:"";position:absolute;left:0;right:0;bottom:22px;height:2px;background:var(--brand)}
.quick-contact{left:1049px;top:32px;width:128px;height:37px;background:var(--brand);color:var(--white);font-size:11px;font-weight:600;display:flex;align-items:center;justify-content:center}

/* hero */
.hero{left:0;top:96px;width:1200px;height:438px;background:linear-gradient(100deg,#3f3d3b 0%,#5a5552 45%,#4a4542 70%,#2e2c2b 100%)}
.hero-phone{left:790px;top:96px;width:340px;height:477px;background:linear-gradient(160deg,#cdb7a3 0%,#b99a82 50%,#8e7463 100%);border-radius:60px 0 0 0}
.hero-kicker{left:119px;top:232px;font-size:13px;font-weight:700;color:var(--white);letter-spacing:.5px}
.hero-title{left:119px;top:262px;font-family:"Jost",sans-serif;font-weight:400;font-size:37px;color:var(--brand);letter-spacing:.5px}
.hero-text{left:119px;top:313px;width:520px;font-size:12.5px;line-height:17px;color:var(--white)}
.hero-btn{left:120px;top:377px;width:135px;height:38px;background:var(--white);color:var(--brand);font-size:11px;font-weight:700;display:flex;align-items:center;justify-content:center;gap:12px}

/* about */
.about-photo{left:0;top:534px;width:637px;height:581px;background:linear-gradient(90deg,#c9c4bf 0%,#8f8a86 45%,#5c5a5c 100%)}
.about-panel{left:637px;top:573px;width:563px;height:542px;background:linear-gradient(135deg,#ececec 0%,#e2e2e2 60%,#d8d8d8 100%)}
.about-frame{left:587px;top:693px;width:128px;height:332px;border:1px solid #7d7d7d;border-right:none}
.about-kicker{left:675px;top:739px;font-family:"Jost",sans-serif;font-weight:600;font-size:22px;color:#555}
.about-title{left:675px;top:772px;font-family:"Jost",sans-serif;font-weight:400;font-size:42px;color:var(--brand);letter-spacing:.5px}
.about-text{left:675px;top:838px;width:410px;font-size:14px;line-height:18px;color:#222}
.small-btn{background:var(--white);color:var(--brand);font-size:9px;font-weight:700;display:flex;align-items:center;justify-content:center}
.about-btn{left:677px;top:959px;width:91px;height:24px}

/* services */
.services-title{left:0;top:1200px;width:1200px;text-align:center;font-family:"Jost",sans-serif;font-size:39px;color:var(--brand);letter-spacing:.5px}
.services-sub{left:0;top:1259px;width:1200px;text-align:center;font-size:13.5px;color:var(--muted)}
.card{width:313px;height:220px}
.card-image{position:absolute;left:0;top:0;width:313px;height:175px}
.card-caption{position:absolute;left:0;top:175px;width:313px;height:45px;background:var(--caption);font-family:"Jost",sans-serif;font-size:14px;color:#777;padding:12px 0 0 22px;letter-spacing:.3px}
.card-feature{background:var(--brand-deep);color:var(--white);padding:36px 30px}
.card-feature h3{font-size:14px;font-weight:600;margin-bottom:20px}
.card-feature p{font-size:11.5px;line-height:18px;margin-bottom:22px;width:240px}
.card-feature .small-btn{width:90px;height:25px}
</style>
</head>
<body>

<header class="site-header abs">
  <div class="brand abs"><span class="brand-mark"></span><span class="brand-name">Harbor Quill</span></div>
  <nav class="main-nav abs">
    <a class="is-active">Home</a><a>What we do</a><a>Products</a><a>About</a><a>Contact</a>
  </nav>
  <div class="quick-contact abs">Quick Contact</div>
</header>

<section class="hero abs" role="img" aria-label="Modern bedroom with desk and shelves, dimmed behind the headline"></section>
<div class="hero-phone abs" role="img" aria-label="Hands holding a smartphone running a smart home control app"></div>
<p class="hero-kicker abs">SMART HOME</p>
<h1 class="hero-title abs">SMART DEVICE INTEGRATION</h1>
<p class="hero-text abs">We are focused on delivering affordable and easily usable devices for your home and office. Wireless smart home - no need for pre-wired cabling</p>
<div class="hero-btn abs">LEARN MORE <svg width="7" height="10" viewBox="0 0 7 10"><path d="M1 1l4 4-4 4" fill="none" stroke="currentColor" stroke-width="1.8"/></svg></div>

<div class="about-photo abs" role="img" aria-label="Person holding a smartphone in a bright living room"></div>
<section class="about-panel abs"></section>
<div class="about-frame abs"></div>
<p class="about-kicker abs">ABOUT</p>
<h2 class="about-title abs">HARBOR QUILL</h2>
<p class="about-text abs">Harbor Quill began as an idea in a garage and a belief that home technology should be readily available and reasonably priced. We are constantly sourcing and experimenting with new technologies and solutions to create any vision of the future you can imagine.</p>
<div class="small-btn about-btn abs">Learn More</div>

<h2 class="services-title abs">SMART DEVICE INTEGRATION</h2>
<p class="services-sub abs">Offering the latest in Smart Home Devices inc</p>

<div class="card card-feature abs" style="left:112px;top:1330px">
  <h3>Home Automation</h3>
  <p>Show us your Vision and we'll create reality, by bringing technology and your home or office together.</p>
  <div class="small-btn">Learn More</div>
</div>
<div class="card abs" style="left:444px;top:1330px"><div class="card-image" role="img" aria-label="Living room with a wall-mounted voice control panel" style="background:linear-gradient(90deg,#dfe3e4,#c9b9a1 55%,#e8e6e2)"></div><div class="card-caption">Voice Control With Kestrel Nova</div></div>
<div class="card abs" style="left:775px;top:1330px"><div class="card-image" role="img" aria-label="Silver keyless door handle lock" style="background:linear-gradient(90deg,#f4f4f4,#c8c8c8 40%,#f7f7f7)"></div><div class="card-caption">Keyless Entry</div></div>

<div class="card abs" style="left:112px;top:1598px"><div class="card-image" role="img" aria-label="Open lounge with large TV and floor speakers" style="background:linear-gradient(180deg,#b8b4ae,#8f8880 60%,#c9c2b8)"></div><div class="card-caption">Home Theatre Design.</div></div>
<div class="card abs" style="left:444px;top:1598px"><div class="card-image" role="img" aria-label="Room with automated sheer curtains and blinds" style="background:linear-gradient(90deg,#6e4a2e,#d9b98c 45%,#a37a4d)"></div><div class="card-caption">Blind and Curtain Automation</div></div>
<div class="card abs" style="left:775px;top:1598px"><div class="card-image" role="img" aria-label="Video doorbell intercom mounted on a textured wall" style="background:linear-gradient(90deg,#a88a6c,#6d5b4c 60%,#a1866b)"></div><div class="card-caption">Video Doorbell and Intercom</div></div>

<div class="card abs" style="left:112px;top:1846px"><div class="card-image" role="img" aria-label="Open garage with a smart roller door" style="background:linear-gradient(180deg,#cfcfcf,#8e8e8e 55%,#5d5d5d)"></div><div class="card-caption">Smart Garage Doors</div></div>
<div class="card abs" style="left:444px;top:1846px"><div class="card-image" role="img" aria-label="Friends on a sofa enjoying home entertainment" style="background:linear-gradient(180deg,#4b3d3a,#7a5d52 55%,#3a3232)"></div><div class="card-caption">Media Entertainment</div></div>
<div class="card abs" style="left:775px;top:1846px"><div class="card-image" role="img" aria-label="Kitchen counter with a smart speaker for multiroom audio" style="background:linear-gradient(90deg,#8fb0c8,#d9e3ea 55%,#b9ccd9)"></div><div class="card-caption">Multiroom Audio</div></div>

<section class="abs" style="left:0;top:2098px;width:1200px;height:133px;background:var(--brand-deep);overflow:hidden">
  <svg class="abs" style="left:0;top:0" width="1200" height="133" viewBox="0 0 1200 133"><path d="M780 0H1200V133H680Z" fill="#2aa3df" opacity=".45"/></svg>
  <p class="abs" style="left:119px;top:47px;width:560px;font-size:17px;line-height:22px;color:var(--white)">We are focused on delivering affordable and easily usable devices for your home and office. Wireless smart home.</p>
  <div class="abs" style="left:951px;top:48px;width:129px;height:37px;background:var(--white);color:#111;font-size:11px;font-weight:700;display:flex;align-items:center;justify-content:center">Get in Touch</div>
</section>

<footer class="abs" style="left:0;top:2231px;width:1200px;height:175px;background:var(--footer)">
  <nav class="abs" style="left:119px;top:57px;display:flex;gap:26px;font-size:11px;color:#3a3f4a">
    <span style="color:var(--brand)">Home</span><span>What we do</span><span>Products</span><span>About</span><span>Contact</span>
  </nav>
  <p class="abs" style="left:119px;top:80px;font-size:11px;color:var(--white)">Allright reserved copyrith © 2018</p>
  <p class="abs" style="left:942px;top:57px;font-size:10px;color:var(--white)">Stay Connected</p>
  <ul class="abs" style="left:860px;top:80px;width:220px;list-style:none;display:flex;flex-wrap:wrap;justify-content:flex-end;gap:6px 12px;font-size:11px;font-weight:700;color:var(--white)">
    <li>Chirpline</li><li>Proflink</li><li>Snapmeadow</li><li>Chatterbay</li>
  </ul>
</footer>

</body>
</html>
```